Picture Ads

We need some banner ads for our home business opportunity, we are evolving from text to picture ads. I have added some examples of what other distributors are using. We are looking for something really eye catching with some good key words and nice bright colours and to include our photo (attached)
Key words to include:
Booming online business
Personal Development and Leadership Industry
Earn an executive income from home
Simple 3 step system
Make up to $5,000 per sale
Not MLM
The size needs to be: 1000 x 35 pixels
13.9 x 4.75 Inches
35.3 x 11.1 cm
I think different platforms accept different sizes, not too familiar with it yet, any guidance welcome. I've clicked project for 2 days if that is to prioritise the order?
Many thanks,
Maren

Industry/Entity Type

Business

```html
<!DOCTYPE html>
<html lang="en">
<head>
<meta charset="utf-8">
<title>Booming Online Business – Banner Ads</title>
<link rel="stylesheet" href="https://fonts.googleapis.com/css2?family=Oswald:wght@500;600&family=PT+Sans:ital,wght@0,400;0,700;1,400&family=Caveat:wght@500&display=swap">
<style>
  :root {
    --page: #ffffff;
    --banner-edge: #6e6e6e;
    --sky-light: #dbeaeb;
    --sky-mid: #c3dcdf;
    --sky-deep: #a9cdd3;
    --sand: #d9cc9f;
    --taupe: #a59680;
    --frame-white: #ffffff;
    --brown-dark: #4a1d0c;
    --brown-text: #35180c;
    --button: #7b6a48;
    --photo-dark: #5a3a2e;
    --photo-warm: #d7a27e;
  }
  * { box-sizing: border-box; margin: 0; padding: 0; }
  html, body {
    width: 1200px; height: 823px; overflow: hidden;
    background: var(--page);
  }
  .banner {
    position: absolute; left: 27px; width: 1143px; height: 361px;
    border: 1px solid var(--banner-edge);
    overflow: hidden;
    background: linear-gradient(100deg, var(--sky-mid) 0%, var(--sky-light) 55%, var(--sky-mid) 100%);
  }
  .banner--swirl { top: 38px; }
  .banner--wave {
    top: 432px;
    background:
      linear-gradient(160deg, rgba(255,255,255,0) 40%, rgba(255,255,255,.55) 60%, rgba(255,255,255,0) 72%),
      linear-gradient(100deg, var(--sky-deep) 0%, var(--sky-light) 60%, var(--sky-mid) 100%);
  }
  .banner__backdrop {
    position: absolute; right: 0; top: 0; width: 780px; height: 100%;
    background: radial-gradient(ellipse at 60% 45%, rgba(255,255,255,.35), rgba(255,255,255,0) 70%);
  }
  .portrait-frame { position: absolute; left: 0; top: 0; width: 420px; height: 361px; }
  .signature {
    position: absolute; left: 92px; top: 278px;
    font-family: "Caveat", cursive; font-weight: 500; font-size: 31px;
    color: var(--brown-text);
    transform: rotate(-11deg); transform-origin: left center;
    text-shadow: 0 0 4px #fff, 0 0 8px #fff, 0 0 12px #fff;
    white-space: nowrap;
  }
  .headline {
    position: absolute; left: 380px; top: 20px; width: 752px;
    text-align: center; white-space: nowrap;
    font-family: "Oswald", sans-serif; font-weight: 600; font-size: 68px;
    letter-spacing: 1px; line-height: 1.1;
    color: var(--brown-dark);
    text-shadow: 2px 0 0 #fff, -2px 0 0 #fff, 0 2px 0 #fff, 0 -2px 0 #fff,
                 2px 2px 0 #fff, -2px -2px 0 #fff, 2px -2px 0 #fff, -2px 2px 0 #fff,
                 4px 5px 6px rgba(0,0,0,.45);
  }
  .tagline {
    position: absolute; left: 390px; top: 128px; width: 710px; height: 48px;
    background: linear-gradient(90deg, rgba(255,255,255,0) 0%, #fff 20%, #fff 80%, rgba(255,255,255,0) 100%);
    text-align: center; white-space: nowrap;
    font-family: "Oswald", sans-serif; font-weight: 500; font-size: 35px; line-height: 48px;
    color: var(--brown-text);
  }
  .benefits {
    position: absolute; left: 415px; top: 198px; list-style: none;
    font-family: "PT Sans", sans-serif; font-size: 30px; line-height: 38px;
    color: var(--brown-text); white-space: nowrap;
  }
  .benefits li { display: flex; align-items: center; gap: 10px; }
  .tick { width: 25px; height: 25px; flex: none; }
  .cta {
    position: absolute; left: 915px; top: 288px; width: 204px; height: 61px;
    background: var(--button); border: 3px solid #fff;
    box-shadow: 0 2px 4px rgba(0,0,0,.35);
    text-align: center; color: #fff;
    font-family: "PT Sans", sans-serif;
  }
  .cta__main { display: block; font-size: 26px; line-height: 30px; margin-top: 3px; }
  .cta__sub { display: block; font-size: 16px; font-style: italic; line-height: 20px; }
</style>
</head>
<body>

<section class="banner banner--swirl">
  <div class="banner__backdrop"></div>
  <svg class="portrait-frame" viewBox="0 0 420 361">
    <path d="M0,0 H175 C120,60 20,110 30,210 C40,290 120,330 150,361 H0 Z" fill="var(--sand)"/>
    <path d="M218,-20 C250,30 400,80 400,190 C400,290 310,320 270,340 L265,361 L171,361 L166,340 C126,320 36,290 36,190 C36,80 186,30 218,-20Z" fill="var(--frame-white)"/>
    <path d="M218,0 C240,40 362,90 362,190 C362,270 300,300 250,320 L245,361 L191,361 L186,320 C136,300 74,270 74,190 C74,90 196,40 218,0Z" fill="var(--taupe)"/>
    <defs>
      <linearGradient id="photoTone1" x1="0" y1="0" x2="1" y2="1">
        <stop offset="0" stop-color="var(--photo-dark)"/>
        <stop offset=".55" stop-color="var(--photo-warm)"/>
        <stop offset="1" stop-color="var(--photo-dark)"/>
      </linearGradient>
    </defs>
    <path role="img" aria-label="Photo of Maren and Delia Hartley" d="M218,38 C240,70 340,110 340,192 C340,262 290,292 218,294 C146,292 96,262 96,192 C96,110 196,70 218,38Z" fill="url(#photoTone1)"/>
  </svg>
  <p class="signature">Maren and Delia Hartley</p>
  <h1 class="headline">Booming Online Business</h1>
  <p class="tagline">Earn an executive income from home</p>
  <ul class="benefits">
    <li><svg class="tick" viewBox="0 0 24 24"><circle cx="12" cy="12" r="12" fill="var(--brown-dark)"/><path d="M6.5,12.5 L10.5,16.5 L17.5,7.5" fill="none" stroke="#fff" stroke-width="3" stroke-linecap="round" stroke-linejoin="round"/></svg>Personal Development and Leadership Industry</li>
    <li><svg class="tick" viewBox="0 0 24 24"><circle cx="12" cy="12" r="12" fill="var(--brown-dark)"/><path d="M6.5,12.5 L10.5,16.5 L17.5,7.5" fill="none" stroke="#fff" stroke-width="3" stroke-linecap="round" stroke-linejoin="round"/></svg>Make Up To $5,000 Per Sale</li>
    <li><svg class="tick" viewBox="0 0 24 24"><circle cx="12" cy="12" r="12" fill="var(--brown-dark)"/><path d="M6.5,12.5 L10.5,16.5 L17.5,7.5" fill="none" stroke="#fff" stroke-width="3" stroke-linecap="round" stroke-linejoin="round"/></svg>Simple 3 Step System</li>
    <li><svg class="tick" viewBox="0 0 24 24"><circle cx="12" cy="12" r="12" fill="var(--brown-dark)"/><path d="M6.5,12.5 L10.5,16.5 L17.5,7.5" fill="none" stroke="#fff" stroke-width="3" stroke-linecap="round" stroke-linejoin="round"/></svg>Not MLM</li>
  </ul>
  <a class="cta"><span class="cta__main">CLICK HERE</span><span class="cta__sub">For More Info</span></a>
</section>

<section class="banner banner--wave">
  <div class="banner__backdrop"></div>
  <svg class="portrait-frame" viewBox="0 0 420 361">
    <path d="M0,0 H175 C120,60 20,110 30,210 C40,290 120,330 150,361 H0 Z" fill="var(--sand)"/>
    <path d="M218,-20 C250,30 400,80 400,190 C400,290 310,320 270,340 L265,361 L171,361 L166,340 C126,320 36,290 36,190 C36,80 186,30 218,-20Z" fill="var(--frame-white)"/>
    <path d="M218,0 C240,40 362,90 362,190 C362,270 300,300 250,320 L245,361 L191,361 L186,320 C136,300 74,270 74,190 C74,90 196,40 218,0Z" fill="var(--taupe)"/>
    <defs>
      <linearGradient id="photoTone2" x1="0" y1="0" x2="1" y2="1">
        <stop offset="0" stop-color="var(--photo-dark)"/>
        <stop offset=".55" stop-color="var(--photo-warm)"/>
        <stop offset="1" stop-color="var(--photo-dark)"/>
      </linearGradient>
    </defs>
    <path role="img" aria-label="Photo of Maren and Delia Hartley" d="M218,38 C240,70 340,110 340,192 C340,262 290,292 218,294 C146,292 96,262 96,192 C96,110 196,70 218,38Z" fill="url(#photoTone2)"/>
  </svg>
  <p class="signature">Maren and Delia Hartley</p>
  <h1 class="headline">Booming Online Business</h1>
  <p class="tagline">Earn an executive income from home</p>
  <ul class="benefits">
    <li><svg class="tick" viewBox="0 0 24 24"><circle cx="12" cy="12" r="12" fill="var(--brown-dark)"/><path d="M6.5,12.5 L10.5,16.5 L17.5,7.5" fill="none" stroke="#fff" stroke-width="3" stroke-linecap="round" stroke-linejoin="round"/></svg>Personal Development and Leadership Industry</li>
    <li><svg class="tick" viewBox="0 0 24 24"><circle cx="12" cy="12" r="12" fill="var(--brown-dark)"/><path d="M6.5,12.5 L10.5,16.5 L17.5,7.5" fill="none" stroke="#fff" stroke-width="3" stroke-linecap="round" stroke-linejoin="round"/></svg>Make Up To $5,000 Per Sale</li>
    <li><svg class="tick" viewBox="0 0 24 24"><circle cx="12" cy="12" r="12" fill="var(--brown-dark)"/><path d="M6.5,12.5 L10.5,16.5 L17.5,7.5" fill="none" stroke="#fff" stroke-width="3" stroke-linecap="round" stroke-linejoin="round"/></svg>Simple 3 Step System</li>
    <li><svg class="tick" viewBox="0 0 24 24"><circle cx="12" cy="12" r="12" fill="var(--brown-dark)"/><path d="M6.5,12.5 L10.5,16.5 L17.5,7.5" fill="none" stroke="#fff" stroke-width="3" stroke-linecap="round" stroke-linejoin="round"/></svg>Not MLM</li>
  </ul>
  <a class="cta"><span class="cta__main">CLICK HERE</span><span class="cta__sub">For More Info</span></a>
</section>

</body>
</html>
```